Business Card Design

Please use the Logo for colors and styles, and create a business card using the following info:

Matthias Lorbeer
Web Developer

Lorbeer Systems
+41 76 418 57 90
matthias@lorbeer-systems.ch
www.lorbeer-systems.ch

Download the logo at http://lorbeer-systems.ch/tl_files/lorbeer_systems.zip

Thanks for your works!

```html
<!DOCTYPE html>
<html lang="en">
<head>
<meta charset="utf-8">
<title>Lorbeer Systems – Business Card</title>
<link href="https://fonts.googleapis.com/css2?family=Jost:wght@400;500&display=swap" rel="stylesheet">
<style>
  :root {
    --navy: #24497a;
    --navy-deep: #1f4170;
    --accent: #2c7cc4;
    --paper: #ffffff;
    --ink-light: #e9eef6;
    --backdrop: #dfe4ea;
  }
  * { margin: 0; padding: 0; box-sizing: border-box; }
  html, body { width: 1200px; height: 960px; overflow: hidden; }
  body {
    background: var(--backdrop);
    font-family: "Jost", "Futura", sans-serif;
    display: flex;
    flex-direction: column;
    align-items: center;
    justify-content: center;
    gap: 60px;
  }
  .card {
    width: 630px;
    height: 360px;
    position: relative;
    overflow: hidden;
    box-shadow: 0 10px 30px rgba(20, 40, 70, 0.18);
  }
  /* Front side */
  .card-front { background: var(--paper); }
  .front-brand {
    height: 178px;
    display: flex;
    align-items: center;
    justify-content: center;
  }
  .wordmark {
    font-weight: 500;
    font-size: 40px;
    letter-spacing: 0.5px;
    text-transform: uppercase;
    color: var(--accent);
  }
  .accent-rule {
    height: 3px;
    background: var(--accent);
  }
  .front-details {
    position: absolute;
    left: 0; right: 0; bottom: 0;
    top: 187px;
    background: var(--navy);
    display: flex;
    align-items: center;
    color: var(--ink-light);
  }
  .identity {
    width: 290px;
    padding-left: 50px;
  }
  .identity .person-name { font-size: 30px; font-weight: 400; line-height: 1.2; }
  .identity .person-role { font-size: 20px; font-weight: 400; margin-top: 6px; }
  .divider {
    width: 1px;
    height: 120px;
    background: linear-gradient(to bottom, transparent, rgba(255,255,255,0.55), transparent);
  }
  .contacts {
    list-style: none;
    padding-left: 50px;
    font-size: 16px;
    line-height: 1.55;
  }
  .contacts li { display: flex; align-items: center; gap: 8px; }
  .contacts svg { width: 12px; height: 12px; fill: var(--ink-light); flex: none; }
  /* Back side */
  .card-back {
    background: var(--navy-deep);
    display: flex;
    align-items: center;
    justify-content: center;
  }
  .card-back .wordmark { color: var(--paper); font-size: 38px; }
</style>
</head>
<body>
  <section class="card card-front">
    <div class="front-brand">
      <span class="wordmark">Lorbeer Systems</span>
    </div>
    <div class="accent-rule"></div>
    <div class="front-details">
      <div class="identity">
        <p class="person-name">Matthias Lorbeer</p>
        <p class="person-role">Web Developer</p>
      </div>
      <div class="divider"></div>
      <ul class="contacts">
        <li>
          <svg viewBox="0 0 24 24" aria-hidden="true"><path d="M6.6 10.8a15.1 15.1 0 0 0 6.6 6.6l2.2-2.2c.3-.3.7-.4 1-.2 1.1.4 2.3.6 3.6.6.6 0 1 .4 1 1V20c0 .6-.4 1-1 1C10.6 21 3 13.4 3 4c0-.6.4-1 1-1h3.5c.6 0 1 .4 1 1 0 1.3.2 2.5.6 3.6.1.3 0 .7-.2 1z"/></svg>
          +41 76 418 57 90
        </li>
        <li>
          <svg viewBox="0 0 24 24" aria-hidden="true"><path d="M2 5h20v14H2z M2 5l10 8 10-8" fill="none" stroke="#e9eef6" stroke-width="2.4"/><path d="M2 6l10 7.5L22 6v13H2z"/></svg>
          matthias@lorbeer-systems.ch
        </li>
        <li>
          <svg viewBox="0 0 24 24" aria-hidden="true"><circle cx="12" cy="12" r="10" fill="none" stroke="#e9eef6" stroke-width="2.4"/><path d="M2 12h20M12 2c3 3 3 17 0 20M12 2c-3 3-3 17 0 20" fill="none" stroke="#e9eef6" stroke-width="2"/></svg>
          www.lorbeer-systems.ch
        </li>
      </ul>
    </div>
  </section>

  <section class="card card-back">
    <span class="wordmark">Lorbeer Systems</span>
  </section>
</body>
</html>
```